Redesign the *Settings* screen for the BrelloZ app.

BrelloZ app is in production, but we need to refresh and redesign the settings screen to be cleaner, easier, more intuitive, and more professional looking.

Project Deadline Extended
Reason: Several designers have requested more time. This will also give time to provide feedback on existing designs.

Requirements
Must have
• Black background, so that the screen is consistent with the rest of the app.

```html
<!DOCTYPE html>
<html lang="en">
<head>
<meta charset="utf-8">
<title>BrelloZ – Settings</title>
<link href="https://fonts.googleapis.com/css2?family=Roboto:wght@400;500&display=swap" rel="stylesheet">
<style>
:root{
  --canvas:#ffffff;
  --screen:#1e1e1e;
  --panel:#2a2a2a;
  --gap:#1a1a1a;
  --bar:#141414;
  --rule:#3a3a3a;
  --text:#ffffff;
  --muted:#8c8c8c;
  --dim:#5e5e5e;
  --accent:#ff9a0a;
  --on:#4cd964;
  --on-track:#2f7a3a;
}
*{box-sizing:border-box;margin:0;padding:0}
html,body{width:1200px;height:910px;overflow:hidden;background:var(--canvas)}
body{position:relative;font-family:"Roboto",Arial,sans-serif;color:var(--text)}
.screen{position:absolute;width:375px;height:814px;background:var(--screen);transform:scale(.8);transform-origin:0 0;overflow:hidden}
.screen--compact{width:340px;height:602px}
.screen--a{left:129px;top:221px}
.screen--b{left:466px;top:164px}
.screen--c{left:810px;top:164px}

.status{height:22px;background:var(--bar);display:flex;align-items:center;justify-content:space-between;padding:0 6px;font-size:12px}
.status__left,.status__right{display:flex;align-items:center;gap:4px;width:120px}
.status__right{justify-content:flex-end}
.battery{width:22px;height:10px;border:1px solid #fff;border-radius:2px;position:relative}
.battery::before{content:"";position:absolute;left:1px;top:1px;bottom:1px;width:8px;background:#fff}
.nav{height:42px;background:var(--bar);display:flex;align-items:center;justify-content:center;font-size:17px;border-bottom:1px solid var(--gap)}

.section{background:var(--panel);padding:0 0 0 29px;margin-bottom:8px}
.section__head{height:62px;display:flex;align-items:center;justify-content:space-between;padding-right:22px;border-bottom:1px solid var(--rule);font-size:16px;font-weight:500}
.info{width:20px;height:20px;border-radius:50%;background:#6b6b6b;color:#2a2a2a;font:italic 500 13px Georgia,serif;display:flex;align-items:center;justify-content:center}

.mount{height:78px;display:flex;align-items:center}
.mount__opt{display:flex;align-items:center;gap:19px;width:171px;font-size:14px;letter-spacing:.3px;color:var(--muted)}
.mount__opt--active{color:var(--text)}

.circle{width:34px;height:34px;border-radius:50%;border:1.5px solid #4a4a4a;display:flex;align-items:center;justify-content:center;flex:none}
.circle--active{background:var(--accent);border-color:var(--accent)}

.locations{height:99px;display:flex;justify-content:space-between;align-items:center;padding-right:22px;margin-left:-4px}
.loc{display:flex;flex-direction:column;align-items:center;gap:10px;font-size:14px;color:var(--dim);width:62px}
.loc--active{color:var(--text)}

.toggle-row{height:61px;display:flex;align-items:center;justify-content:space-between;padding-right:22px;font-size:13px;font-weight:500}
.switch{width:38px;height:12px;border-radius:6px;background:#555;position:relative}
.switch::after{content:"";position:absolute;top:-6px;left:-4px;width:24px;height:24px;border-radius:50%;background:#bdbdbd}
.switch--on{background:var(--on-track)}
.switch--on::after{left:auto;right:-4px;background:var(--on)}

.actions{height:118px;display:flex;align-items:center;justify-content:space-between;padding:0 24px 0 28px;margin-top:-8px}
.action{display:flex;align-items:center;gap:9px;color:var(--dim)}
.action--active{color:var(--text)}
.action__label{font-size:14px;line-height:1.05}
.action__label small{display:block;font-size:8px;opacity:.85}

.row{margin-left:29px;border-top:1px solid var(--rule);display:flex;align-items:center;justify-content:space-between;padding-right:24px;font-size:13px}
.row--version{height:59px}
.row--logout{height:82px;font-weight:500}

.tabs{position:absolute;left:0;right:0;bottom:0;height:49px;background:var(--panel);display:flex;justify-content:space-around;align-items:center;padding:0 4px}
.tab{display:flex;flex-direction:column;align-items:center;gap:1px;font-size:9px;color:var(--muted);width:60px}
.tab--active{color:var(--accent)}

.screen--compact .section{padding-left:27px}
.screen--compact .mount{height:65px}
.screen--compact .section__head{height:56px;font-size:14px;padding-right:20px}
.screen--compact .locations{height:90px;padding-right:20px}
.screen--compact .toggle-row{height:55px}
.screen--compact .mount__opt{width:154px;font-size:13px;gap:16px}
.screen--compact .actions{height:107px;padding:0 22px 0 26px}
.screen--compact .action__label{font-size:13px}
.screen--compact .row{margin-left:27px;font-size:12px}
.screen--compact .row--version{height:55px}
.screen--compact .tabs{height:45px}
</style>
</head>
<body>

<section class="screen screen--compact screen--a" aria-label="Settings screen, compact">
  <div class="status"><span class="status__left">●●●○○ Nimbus</span><span>9:41 AM</span><span class="status__right">42% <i class="battery"></i></span></div>
  <div class="nav">Settings</div>
  <div class="section">
    <div class="mount">
      <div class="mount__opt mount__opt--active"><span class="circle circle--active"><svg width="16" height="16" viewBox="0 0 16 16"><path d="M3 14V9a5 5 0 0 1 5-5h5M10 1l3 3-3 3" fill="none" stroke="#222" stroke-width="1.6"/></svg></span>Forwards</div>
      <div class="mount__opt"><span class="circle"><svg width="16" height="16" viewBox="0 0 16 16"><path d="M13 14V9a5 5 0 0 0-5-5H3M6 1 3 4l3 3" fill="none" stroke="#555" stroke-width="1.4"/></svg></span>Backwards</div>
    </div>
  </div>
  <div class="section">
    <div class="section__head">Device Mount Location <span class="info">i</span></div>
    <div class="locations">
      <div class="loc"><span class="circle"><svg width="12" height="12" viewBox="0 0 12 12"><path d="M2 2l4 4 4-4M2 6l4 4 4-4" fill="none" stroke="#555" stroke-width="1.5"/></svg></span>Bottom</div>
      <div class="loc loc--active"><span class="circle circle--active"><svg width="12" height="12" viewBox="0 0 12 12"><path d="M2 10l4-4 4 4M2 6l4-4 4 4" fill="none" stroke="#222" stroke-width="1.6"/></svg></span>Top</div>
      <div class="loc"><span class="circle"><svg width="12" height="12" viewBox="0 0 12 12"><path d="M6 2 2 6l4 4M10 2 6 6l4 4" fill="none" stroke="#555" stroke-width="1.5"/></svg></span>Left</div>
      <div class="loc"><span class="circle"><svg width="12" height="12" viewBox="0 0 12 12"><path d="M2 2l4 4-4 4M6 2l4 4-4 4" fill="none" stroke="#555" stroke-width="1.5"/></svg></span>Right</div>
    </div>
  </div>
  <div class="section">
    <div class="section__head">Bullseye Mode <span class="info">i</span></div>
    <div class="toggle-row">OFF <span class="switch"></span></div>
  </div>
  <div class="actions">
    <div class="action"><span class="circle"><svg width="18" height="18" viewBox="0 0 18 18"><path d="M3 9a6 6 0 0 1 10-4.5M15 9a6 6 0 0 1-10 4.5" fill="none" stroke="#555" stroke-width="1.4"/></svg></span><span class="action__label">Sync<small>Account data</small></span></div>
    <div class="action action--active"><span class="circle circle--active"></span><span class="action__label">Linkwave<small>Disconnect</small></span></div>
    <div class="action"><span class="circle"><svg width="14" height="14" viewBox="0 0 14 14"><path d="M3 1v12M3 2l8 4-8 4" fill="#555" stroke="#555" stroke-width="1.3"/></svg></span><span class="action__label">Report<small>Issue</small></span></div>
  </div>
  <div class="row row--version">App Version: 2.3.9.05</div>
  <nav class="tabs">
    <span class="tab tab--active"><svg width="24" height="24" viewBox="0 0 24 24" fill="none" stroke="currentColor"><circle cx="12" cy="12" r="10"/><circle cx="12" cy="12" r="6.5"/><circle cx="12" cy="12" r="3"/></svg>Train</span>
    <span class="tab"><svg width="24" height="24" viewBox="0 0 24 24" fill="none" stroke="currentColor"><rect x="3" y="5" width="18" height="16"/><path d="M3 9h18M8 3v4M16 3v4M7 13h10M7 17h10"/></svg>History</span>
    <span class="tab"><svg width="28" height="24" viewBox="0 0 28 24" fill="none" stroke="currentColor"><path d="M2 8l12-5 12 5-12 5zM7 10v6c4 3 10 3 14 0v-6M24 9v8"/></svg>Learn</span>
    <span class="tab"><svg width="24" height="24" viewBox="0 0 24 24" fill="none" stroke="currentColor"><circle cx="12" cy="12" r="3.5"/><path d="M12 2v3M12 19v3M2 12h3M19 12h3M5 5l2 2M17 17l2 2M5 19l2-2M17 7l2-2"/><circle cx="12" cy="12" r="7"/></svg>Settings</span>
  </nav>
</section>

<section class="screen screen--b" aria-label="Settings screen, Bullseye on">
  <div class="status"><span class="status__left">●●●○○ Nimbus</span><span>9:41 AM</span><span class="status__right">42% <i class="battery"></i></span></div>
  <div class="nav">Settings</div>
  <div class="section">
    <div class="section__head">Device Mount Position <span class="info">i</span></div>
    <div class="mount">
      <div class="mount__opt mount__opt--active"><span class="circle circle--active"><svg width="16" height="16" viewBox="0 0 16 16"><path d="M3 14V9a5 5 0 0 1 5-5h5M10 1l3 3-3 3" fill="none" stroke="#222" stroke-width="1.6"/></svg></span>Forwards</div>
      <div class="mount__opt"><span class="circle"><svg width="16" height="16" viewBox="0 0 16 16"><path d="M13 14V9a5 5 0 0 0-5-5H3M6 1 3 4l3 3" fill="none" stroke="#555" stroke-width="1.4"/></svg></span>Backwards</div>
    </div>
  </div>
  <div class="section">
    <div class="section__head">Device Mount Location <span class="info">i</span></div>
    <div class="locations">
      <div class="loc"><span class="circle"><svg width="12" height="12" viewBox="0 0 12 12"><path d="M2 2l4 4 4-4M2 6l4 4 4-4" fill="none" stroke="#555" stroke-width="1.5"/></svg></span>Bottom</div>
      <div class="loc loc--active"><span class="circle circle--active"><svg width="12" height="12" viewBox="0 0 12 12"><path d="M2 10l4-4 4 4M2 6l4-4 4 4" fill="none" stroke="#222" stroke-width="1.6"/></svg></span>Top</div>
      <div class="loc"><span class="circle"><svg width="12" height="12" viewBox="0 0 12 12"><path d="M6 2 2 6l4 4M10 2 6 6l4 4" fill="none" stroke="#555" stroke-width="1.5"/></svg></span>Left</div>
      <div class="loc"><span class="circle"><svg width="12" height="12" viewBox="0 0 12 12"><path d="M2 2l4 4-4 4M6 2l4 4-4 4" fill="none" stroke="#555" stroke-width="1.5"/></svg></span>Right</div>
    </div>
  </div>
  <div class="section">
    <div class="section__head">Bullseye Mode <span class="info">i</span></div>
    <div class="toggle-row">ON <span class="switch switch--on"></span></div>
  </div>
  <div class="actions">
    <div class="action"><span class="circle"><svg width="18" height="18" viewBox="0 0 18 18"><path d="M3 9a6 6 0 0 1 10-4.5M15 9a6 6 0 0 1-10 4.5" fill="none" stroke="#555" stroke-width="1.4"/></svg></span><span class="action__label">Sync<small>Account data</small></span></div>
    <div class="action action--active"><span class="circle circle--active"></span><span class="action__label">Linkwave<small>Disconnect</small></span></div>
    <div class="action"><span class="circle"><svg width="14" height="14" viewBox="0 0 14 14"><path d="M3 1v12M3 2l8 4-8 4" fill="#555" stroke="#555" stroke-width="1.3"/></svg></span><span class="action__label">Report<small>Issue</small></span></div>
  </div>
  <div class="row row--version">App Version: 2.3.9.05</div>
  <div class="row row--logout">LOG OUT <svg width="32" height="32" viewBox="0 0 32 32" fill="none" stroke="var(--accent)" stroke-width="1.4"><path d="M10 8a12 12 0 1 0 12 0M16 2v13"/></svg></div>
  <nav class="tabs">
    <span class="tab tab--active"><svg width="24" height="24" viewBox="0 0 24 24" fill="none" stroke="currentColor"><circle cx="12" cy="12" r="10"/><circle cx="12" cy="12" r="6.5"/><circle cx="12" cy="12" r="3"/></svg>Train</span>
    <span class="tab"><svg width="24" height="24" viewBox="0 0 24 24" fill="none" stroke="currentColor"><rect x="3" y="5" width="18" height="16"/><path d="M3 9h18M8 3v4M16 3v4M7 13h10M7 17h10"/></svg>History</span>
    <span class="tab"><svg width="28" height="24" viewBox="0 0 28 24" fill="none" stroke="currentColor"><path d="M2 8l12-5 12 5-12 5zM7 10v6c4 3 10 3 14 0v-6M24 9v8"/></svg>Learn</span>
    <span class="tab"><svg width="24" height="24" viewBox="0 0 24 24" fill="none" stroke="currentColor"><circle cx="12" cy="12" r="3.5"/><path d="M12 2v3M12 19v3M2 12h3M19 12h3M5 5l2 2M17 17l2 2M5 19l2-2M17 7l2-2"/><circle cx="12" cy="12" r="7"/></svg>Settings</span>
  </nav>
</section>

<section class="screen screen--c" aria-label="Settings screen, Bullseye off">
  <div class="status"><span class="status__left">●●●○○ Nimbus</span><span>9:41 AM</span><span class="status__right">42% <i class="battery"></i></span></div>
  <div class="nav">Settings</div>
  <div class="section">
    <div class="section__head">Device Mount Position <span class="info">i</span></div>
    <div class="mount">
      <div class="mount__opt mount__opt--active"><span class="circle circle--active"><svg width="16" height="16" viewBox="0 0 16 16"><path d="M3 14V9a5 5 0 0 1 5-5h5M10 1l3 3-3 3" fill="none" stroke="#222" stroke-width="1.6"/></svg></span>Forwards</div>
      <div class="mount__opt"><span class="circle"><svg width="16" height="16" viewBox="0 0 16 16"><path d="M13 14V9a5 5 0 0 0-5-5H3M6 1 3 4l3 3" fill="none" stroke="#555" stroke-width="1.4"/></svg></span>Backwards</div>
    </div>
  </div>
  <div class="section">
    <div class="section__head">Device Mount Location <span class="info">i</span></div>
    <div class="locations">
      <div class="loc"><span class="circle"><svg width="12" height="12" viewBox="0 0 12 12"><path d="M2 2l4 4 4-4M2 6l4 4 4-4" fill="none" stroke="#555" stroke-width="1.5"/></svg></span>Bottom</div>
      <div class="loc loc--active"><span class="circle circle--active"><svg width="12" height="12" viewBox="0 0 12 12"><path d="M2 10l4-4 4 4M2 6l4-4 4 4" fill="none" stroke="#222" stroke-width="1.6"/></svg></span>Top</div>
      <div class="loc"><span class="circle"><svg width="12" height="12" viewBox="0 0 12 12"><path d="M6 2 2 6l4 4M10 2 6 6l4 4" fill="none" stroke="#555" stroke-width="1.5"/></svg></span>Left</div>
      <div class="loc"><span class="circle"><svg width="12" height="12" viewBox="0 0 12 12"><path d="M2 2l4 4-4 4M6 2l4 4-4 4" fill="none" stroke="#555" stroke-width="1.5"/></svg></span>Right</div>
    </div>
  </div>
  <div class="section">
    <div class="section__head">Bullseye Mode <span class="info">i</span></div>
    <div class="toggle-row">OFF <span class="switch"></span></div>
  </div>
  <div class="actions">
    <div class="action"><span class="circle"><svg width="18" height="18" viewBox="0 0 18 18"><path d="M3 9a6 6 0 0 1 10-4.5M15 9a6 6 0 0 1-10 4.5" fill="none" stroke="#555" stroke-width="1.4"/></svg></span><span class="action__label">Sync<small>Account data</small></span></div>
    <div class="action action--active"><span class="circle circle--active"></span><span class="action__label">Linkwave<small>Disconnect</small></span></div>
    <div class="action"><span class="circle"><svg width="14" height="14" viewBox="0 0 14 14"><path d="M3 1v12M3 2l8 4-8 4" fill="#555" stroke="#555" stroke-width="1.3"/></svg></span><span class="action__label">Report<small>Issue</small></span></div>
  </div>
  <div class="row row--version">App Version: 2.3.9.05</div>
  <div class="row row--logout">LOG OUT <svg width="32" height="32" viewBox="0 0 32 32" fill="none" stroke="var(--accent)" stroke-width="1.4"><path d="M10 8a12 12 0 1 0 12 0M16 2v13"/></svg></div>
  <nav class="tabs">
    <span class="tab tab--active"><svg width="24" height="24" viewBox="0 0 24 24" fill="none" stroke="currentColor"><circle cx="12" cy="12" r="10"/><circle cx="12" cy="12" r="6.5"/><circle cx="12" cy="12" r="3"/></svg>Train</span>
    <span class="tab"><svg width="24" height="24" viewBox="0 0 24 24" fill="none" stroke="currentColor"><rect x="3" y="5" width="18" height="16"/><path d="M3 9h18M8 3v4M16 3v4M7 13h10M7 17h10"/></svg>History</span>
    <span class="tab"><svg width="28" height="24" viewBox="0 0 28 24" fill="none" stroke="currentColor"><path d="M2 8l12-5 12 5-12 5zM7 10v6c4 3 10 3 14 0v-6M24 9v8"/></svg>Learn</span>
    <span class="tab"><svg width="24" height="24" viewBox="0 0 24 24" fill="none" stroke="currentColor"><circle cx="12" cy="12" r="3.5"/><path d="M12 2v3M12 19v3M2 12h3M19 12h3M5 5l2 2M17 17l2 2M5 19l2-2M17 7l2-2"/><circle cx="12" cy="12" r="7"/></svg>Settings</span>
  </nav>
</section>

</body>
</html>
```